Tarno Booking website (www.tarnobooking.example)

My company develops booking software, Tarno Booking, for the hourly booking of resources such as classes in a school or customer booking involving rooms in a spa. These bookings also involve the customers, staff, rooms and a lesson or treatment.

The main difference between this software and general calendar software such as Plume calendar is that this Tarno Booking allows resources such as people and rooms to be associated with the bookings. This is important for example in the case of a Spa to make sure the rooms are booked appropriately and to see the free times for the rooms. For a golf practice range the players much be booked to the tee spots where they practice golf.

I have tried to design the website myself, as a computer programmer- I am a bit "square" and not a designer, my first attempt is http://www.tarnobooking.example/, my second attempt is at http://www.welmex-works.example/tarnobookingwebsite/
I am not happy with my designs as compared to the professional designs I see people can come up with here. The software must have the image of a professional software product in order to inspire the confidence of customers.

Am looking for a design which will be the most likely to give the customer the following feeling:
* Confident the product can do the job.
* Feel easy to want to try it, at least for the free trial.
* Its a professional software product and also a web based product, the user can login from the web.

Look at other booking software websites for ideas, here is a list of links to similar booking products. These products all have different features but are mostly for resource booking.
http://welmex-works.example/tarnobookingwebsite/?page=compare
Updates

Hello all,

Thankyou for the designs so far, to save peoples time, I will try to eliminate the bottom 50% of designs now.

To be honest, most of the designs are of a good or high quality, I think its very tough on you as graphic and web designers. Only a minor few are of low quality.

If your design is discarded - I would say its unlikely that you are going to be able to produce a design that will beat the competition. 
You probably already know, you could try to re-sell your design later for other projects or as a template on one of those template websites. Some of these discarded designs are quite worthwhile designs.

Best regards, Dunstan

Target Market(s)

Spa, Gym, School, Golf, any organization who manages bookings of their customers

Industry/Entity Type

Software

Requirements
Must have
• Home page and inner page, any other pages up to you.

Make a logo or use the image of the girl that I already have on the second design.

Menu(s) for navigation.

A language switcher for 3 languages, English, Chinese Traditional and Chinese Simplified. (Western, Hong Kong and Chinese mainland market are important).

Space for a video introduction, it could be small and when the user clicks on it then it gets bigger then it won't take up too much space. Up to you.

A space for the user to login and register a new account.

Screenshots.

I don't have any strong preferences, use your own ideas, if you look at all the other products you can get the basic idea from them.

The total goal is to make a website which is going to lead to sales of the software product.

```html
<!DOCTYPE html>
<html lang="en">
<head>
<meta charset="utf-8">
<title>Tarno Booking</title>
<link rel="stylesheet" href="https://fonts.googleapis.com/css2?family=Open+Sans:wght@300;400;600;700&family=Arimo:wght@400;700&display=swap">
<style>
:root{
  --blue:#0e6a98;
  --blue-dark:#0a5a84;
  --blue-active:#4fb4e2;
  --navy:#0c1423;
  --text:#333;
  --grey-link:#666;
  --green:#7dbb2a;
  --cyan:#3fa9d9;
  --pink:#d9406e;
  --olive:#6b8a12;
  --card-orange:#e58d63;
  --card-blue:#45a3d9;
  --card-teal:#4fbfb6;
  --card-red:#de5d6c;
}
*{box-sizing:border-box;margin:0;padding:0}
html,body{width:1047px;height:1200px;overflow:hidden;background:#fff}
body{font-family:"Arimo",Arial,sans-serif;color:var(--text);position:relative}
.stage{position:absolute;left:17px;top:24px;width:1012px;height:1150px;transform:scale(1.02);transform-origin:0 0}
.abs{position:absolute}
.topbar{left:0;top:0;width:1012px;height:60px;background:linear-gradient(#fff,#ececec)}
.brand{left:30px;top:10px;display:flex;align-items:center;gap:10px}
.brand-dot{width:38px;height:38px;border-radius:50%;background:var(--green)}
.brand-name{font-family:"Open Sans",sans-serif;font-weight:700;font-size:30px;color:#333;letter-spacing:-1px}
.login{left:455px;top:12px;width:373px;height:38px;background:var(--blue);border-radius:6px;display:flex;align-items:center;padding:0 7px;gap:7px}
.login .field{height:24px;background:#fff;border:1px solid #9ab;font-size:9px;color:#556;padding:6px 6px 0;width:114px}
.login .btn{height:24px;background:linear-gradient(#fff,#ddd);border:1px solid #9ab;font-size:9px;color:#444;padding:6px 6px 0}
.login .reg{color:#fff;font-family:"Open Sans",sans-serif;font-size:13px;margin-left:4px}
.lang{left:836px;top:12px;width:128px;height:36px;background:#e6e6e6;border-radius:4px;padding:8px}
.lang .select{width:82px;height:18px;background:#fff;border:1px solid #ccc;font-size:9px;padding:3px 4px;position:relative}
.lang .select:after{content:"";position:absolute;right:4px;top:7px;border:3px solid transparent;border-top-color:#333}
.lang .flag{position:absolute;left:97px;top:12px;width:21px;height:14px;background:#3b5aa8}
.panel{left:20px;top:60px;width:960px;height:1075px;background:#fff;box-shadow:0 0 6px rgba(0,0,0,.25)}
.util{right:48px;top:94px;display:flex;align-items:center;font-family:"Open Sans",sans-serif;font-size:13.5px;color:var(--grey-link)}
.util .sep{margin:0 12px}
.util .cta{display:flex;align-items:center;gap:6px;margin-left:14px;color:#444}
.util .cta:first-of-type{margin-left:20px}
.nav{left:20px;top:145px;width:960px;height:51px;background:linear-gradient(var(--blue),var(--blue-dark));display:flex;padding-left:30px}
.nav a{color:#fff;text-decoration:none;font-family:"Open Sans",sans-serif;font-size:14.5px;display:flex;align-items:center;justify-content:center;border-right:1px solid rgba(0,0,0,.25);height:51px}
.nav a.active{background:var(--blue-active);margin-top:-4px;height:55px}
.hero{left:20px;top:196px;width:960px;height:310px;background:var(--navy)}
.hero-photo{position:absolute;right:0;top:0;width:540px;height:310px;background:radial-gradient(circle at 58% 15%,#8fc8ff 0,#2c5c9a 18%,#15294a 48%,var(--navy) 80%)}
.hero h1{position:absolute;left:37px;top:82px;font-family:"Open Sans",sans-serif;font-weight:300;font-size:26px;line-height:42px;color:#fff}
.hero h1 .b1{color:#bbb;font-weight:600}.hero h1 .b2{font-weight:600}
.welcome{left:43px;top:526px;width:535px}
.welcome h2{font-size:23px;color:#333;margin-bottom:10px;font-weight:700}
.welcome h2 span{color:#000}
.welcome p{font-size:11.6px;line-height:15.9px;color:#111;margin-bottom:16px}
.welcome a{color:#1a6ec1}
.intro-art{left:95px;top:724px;width:90px;height:100px;background:linear-gradient(#f3d08a,#c23b3b);border-radius:8px}
.intro-cap{left:43px;top:840px;width:172px;text-align:center;font-size:16px;font-weight:700;line-height:21px;color:#444}
.video{left:238px;top:719px;width:306px;height:172px;background:#8c8c8c;border:1px solid #777;border-radius:3px}
.video .play{position:absolute;left:134px;top:56px}
.video .label{position:absolute;left:0;width:100%;top:96px;text-align:center;color:#fff;font-size:17px;font-weight:700}
.testimonials{left:610px;top:521px;width:358px;height:376px;background:linear-gradient(90deg,#fff,#e9e9e9);border-left:2px solid #ccc}
.testimonials h3{position:absolute;left:76px;top:22px;font-size:16.5px;color:#333}
.quote{position:absolute;left:8px;width:340px}
.quote .logo{position:absolute;left:0;top:0;width:88px;height:62px;background:#fff;border-radius:4px;display:flex;align-items:center;justify-content:center;font-size:13px;font-weight:700;color:#b11}
.quote p{position:absolute;left:97px;top:0;width:230px;font-size:11.6px;line-height:15.2px;color:#111}
.quote .who{position:absolute;left:96px;top:64px;font-size:13px;font-weight:700;color:var(--olive)}
.quote .role{position:absolute;left:96px;top:82px;font-size:10.5px;color:#111}
.testimonials hr{position:absolute;left:8px;top:178px;width:336px;border:0;border-top:1px solid #bbb}
.all-btn{position:absolute;left:103px;top:324px;width:140px;height:33px;background:var(--blue);border-radius:4px;color:#fff;font-size:12px;text-align:center;line-height:33px}
.card{top:920px;width:207px;height:131px;border:1px solid #ddd;border-radius:3px;background:linear-gradient(#fafafa,#e4e4e4);overflow:hidden}
.card .art{position:absolute;left:60px;top:10px;width:86px;height:76px;border-radius:6px}
.card .label{position:absolute;left:2px;right:2px;bottom:2px;height:44px;color:#fff;font-weight:700;font-size:15.5px;line-height:17px;display:flex;align-items:center;justify-content:center;text-align:center}
.footer{left:20px;top:1080px;width:960px;height:55px;background:var(--blue)}
.footer .strip{position:absolute;left:0;top:0;width:100%;height:4px;background:linear-gradient(90deg,#e8786b 0 15%,#7a7fc7 15% 28%,#f2c36b 28% 45%,#4fbfb6 45% 59%,#e8786b 59% 75%,#f2c36b 75% 90%,#4fb4e2 90%)}
.footer .ctas{position:absolute;left:20px;top:19px;display:flex;gap:10px;font-family:"Open Sans",sans-serif;font-size:13.5px;color:#fff}
.footer .ctas span{display:flex;align-items:center;gap:5px}
.footer .divider{position:absolute;left:356px;top:4px;width:1px;height:51px;background:rgba(255,255,255,.3)}
.footer .links{position:absolute;left:376px;top:14px;font-size:12px;line-height:18px;color:#fff;white-space:pre}
</style>
</head>
<body>
<div class="stage">
  <header class="abs topbar"></header>
  <div class="abs brand"><span class="brand-dot"></span><span class="brand-name">TarnoBooking</span></div>
  <form class="abs login">
    <span class="field">USER ID</span><span class="field">PASSWORD</span><span class="btn">LOGIN</span><span class="reg">Register</span>
  </form>
  <div class="abs lang"><div class="select">English</div><span class="flag"></span></div>

  <main class="abs panel"></main>

  <nav class="abs util">
    <span>About Tarno Booking</span><span class="sep">|</span><span>Videos</span><span class="sep">|</span><span>Documentation</span>
    <span class="cta"><svg width="22" height="22"><circle cx="11" cy="11" r="11" fill="#7dbb2a"/><path d="M11 5v9M7 10l4 4 4-4" stroke="#fff" stroke-width="2.4" fill="none"/></svg>FREE TRIAL</span>
    <span class="cta"><svg width="22" height="22"><circle cx="11" cy="11" r="11" fill="#3fa9d9"/><path d="M5 7h2l2 7h7l1.5-5H8" stroke="#fff" stroke-width="1.6" fill="none"/><circle cx="10" cy="16.5" r="1.2" fill="#fff"/><circle cx="15" cy="16.5" r="1.2" fill="#fff"/></svg>PURCHASE</span>
    <span class="cta"><svg width="22" height="22"><circle cx="11" cy="11" r="11" fill="#d9406e"/><path d="M6 11l4 4 7-8" stroke="#fff" stroke-width="2.6" fill="none"/></svg>COMPARE</span>
  </nav>

  <nav class="abs nav">
    <a class="active" style="width:174px">General Introduction</a>
    <a style="width:103px">Features</a>
    <a style="width:189px">2 Minute Introduction</a>
    <a style="width:192px">10 Minute Introduction</a>
    <a style="width:125px">White Paper</a>
    <a style="width:127px;border-right:0">Trial Version</a>
  </nav>

  <section class="abs hero">
    <div class="hero-photo" role="img" aria-label="Hand touching glowing floating screens"></div>
    <h1><span class="b1">Tarno</span><span class="b2">Booking</span> is front office booking software<br>which makes managing bookings, room<br>and staff availability fast and simple.</h1>
  </section>

  <section class="abs welcome">
    <h2>Welcome to Tarno<span>Booking</span></h2>
    <p>Tarno Booking is front office booking software which makes managing bookings, room and staff availability fast and simple. We focus on producing quality software which is powerful yet easy to use. This is suitable for many types of business, <a href="#">click here to view all the available business types and to learn more about how this software can help you directly</a>.</p>
    <p>Tarno Booking stores all data on our servers in the SaaS model giving a very low total cost of owner-ship our customers. You have zero investment in server platform hardware, zero investment in software licenses, zero investment in hardware and software upgrades, as these are included as part of the service.</p>
  </section>
  <div class="abs intro-art" role="img" aria-label="Cartoon presenter holding a calendar"></div>
  <div class="abs intro-cap">Let me Introduce<br>Tarno<span style="color:#000">Booking</span></div>
  <div class="abs video" role="img" aria-label="Video preview of the booking workflow">
    <svg class="play" width="38" height="38"><circle cx="19" cy="19" r="18" fill="#fff"/><circle cx="19" cy="19" r="15" fill="#1f63c6"/><path d="M15 11l11 8-11 8z" fill="#fff"/></svg>
    <div class="label">Play Video</div>
  </div>

  <aside class="abs testimonials">
    <h3>Client Testimonials</h3>
    <div class="quote" style="top:60px">
      <div class="logo">Gearline</div>
      <p>Lorem Ipsum is simply dummy text of the printing and typesetting industry. Lorem Ipsum has been the industry's standard dummy text ever since the 1500s, when</p>
      <div class="who">Owen Marsh</div><div class="role">Business Development</div>
    </div>
    <hr>
    <div class="quote" style="top:203px">
      <div class="logo" style="color:#222">Roadhaus</div>
      <p>Lorem Ipsum is simply dummy text of the printing and typesetting industry. Lorem Ipsum has been the industry's standard dummy text ever since the 1500s, when</p>
      <div class="who">Nina Kerr</div><div class="role">Business Development</div>
    </div>
    <div class="all-btn">View All Testimonials</div>
  </aside>

  <div class="abs card" style="left:32px"><div class="art" role="img" aria-label="Cartoon character peeking" style="background:#f1e3c6"></div><div class="label" style="background:var(--card-orange)">See Waht our<br>clients are saying!</div></div>
  <div class="abs card" style="left:280px"><div class="art" role="img" aria-label="Free trial software box" style="background:linear-gradient(#5fb7e6,#f0b43a)"></div><div class="label" style="background:var(--card-blue)">Get a FREE TRIAL</div></div>
  <div class="abs card" style="left:530px"><div class="art" role="img" aria-label="Software box with disc" style="background:linear-gradient(#4aa8de,#c9ccd2)"></div><div class="label" style="background:var(--card-teal)">Fast, Easy and Affordable<br>Software</div></div>
  <div class="abs card" style="left:763px"><svg class="abs" style="left:66px;top:12px" width="76" height="64"><path d="M6 34l20 20L70 8" stroke="#4fae1f" stroke-width="14" fill="none" stroke-linejoin="round"/></svg><div class="label" style="background:var(--card-red)">Proof that we’re<br>really good</div></div>

  <footer class="abs footer">
    <div class="strip"></div>
    <div class="ctas">
      <span><svg width="22" height="22"><circle cx="11" cy="11" r="11" fill="#7dbb2a"/><path d="M11 5v9M7 10l4 4 4-4" stroke="#fff" stroke-width="2.4" fill="none"/></svg>FREE TRIAL</span>
      <span><svg width="22" height="22"><circle cx="11" cy="11" r="11" fill="#7cc6ea"/><path d="M5 7h2l2 7h7l1.5-5H8" stroke="#fff" stroke-width="1.6" fill="none"/></svg>PURCHASE</span>
      <span><svg width="22" height="22"><circle cx="11" cy="11" r="11" fill="#d9406e"/><path d="M6 11l4 4 7-8" stroke="#fff" stroke-width="2.6" fill="none"/></svg>COMPARE</span>
    </div>
    <div class="divider"></div>
    <div class="links">About TarnoBooking     |     Videos     |     Documentation     |     General Introduction     |     Features
2 Minute Introduction     |     10 Minute Introduction          |     White Paper     |     Trial Version</div>
  </footer>
</div>
</body>
</html>
```